Commercial/Retail/Office Real Estate Lease Brochure for Vacant Space

We need a commercial Real Estate Fyler Template for lease space. We would like it for Vacant lease spaces and new buildings in the commercial, retail, office and industrial lease space. The flyer should have sections for: Highlights (site size, leasable area, Location, Ammenties etc.), concept floor plan or site plan, contact information, project/construction description.

Target Market(s)

Commercial Leasing for Offices and Retail Space

Industry/Entity Type

Real Estate Leasing and Development

Requirements
Must have
• Clean, timeless not overly busy template with spots for key metrics (square feet leaseable space, parking etc), location for pictures
Nice to have
• Lorvex Crane Real Estate Logo for header/foot, reusable with adjustments for other spaces
Should not have
• Busy, overall colorfull or contrasting

```html
<!DOCTYPE html>
<html lang="en">
<head>
<meta charset="utf-8">
<title>Commercial Leasing Opportunity – Lorvex Crane Real Estate</title>
<link href="https://fonts.googleapis.com/css2?family=Encode+Sans+Condensed:wght@300;400;600;700&family=Open+Sans:wght@400;600&display=swap" rel="stylesheet">
<style>
  :root {
    --canvas: #e6e6e6;
    --paper: #ffffff;
    --ink: #1a1a1a;
    --heading-grey: #8a8a8a;
    --body-grey: #8c8c8c;
    --bullet: #c4c4c4;
    --band: #050505;
    --panel: #1f2024;
    --panel-label: #b9bcc2;
    --map-light: #f1f1f1;
    --map-mid: #e4e4e4;
    --white: #ffffff;
  }
  * { margin: 0; padding: 0; box-sizing: border-box; }
  html, body { width: 1200px; height: 844px; overflow: hidden; }
  body {
    background: var(--canvas);
    position: relative;
    font-family: "Open Sans", Arial, sans-serif;
  }
  .sheet {
    position: absolute;
    top: 128px;
    width: 432px;
    height: 560px;
    background: var(--paper);
    overflow: hidden;
  }
  .sheet--plan { left: 148px; }
  .sheet--cover { left: 664px; }

  .section-title {
    position: absolute;
    font-family: "Encode Sans Condensed", "Arial Narrow", sans-serif;
    font-weight: 300;
    font-size: 22px;
    color: var(--heading-grey);
    letter-spacing: -0.2px;
    white-space: nowrap;
  }

  /* Plan sheet */
  .plan-title { left: 22px; top: 10px; }
  .floor-plan {
    position: absolute; left: 16px; top: 44px; width: 404px; height: 270px;
    background: linear-gradient(90deg, #9a9a9a 0 38%, #f1f1f1 38% 100%);
    border: 1px solid #444;
  }
  .description-title { left: 24px; top: 330px; }
  .fact-list {
    position: absolute; left: 20px; top: 378px;
    list-style: none;
    font-family: "Encode Sans Condensed", "Arial Narrow", sans-serif;
    font-size: 8.6px; line-height: 10.2px; color: var(--body-grey);
    white-space: nowrap;
  }
  .fact-list li { position: relative; padding-left: 10px; }
  .fact-list li::before {
    content: ""; position: absolute; left: 1px; top: 3.5px;
    width: 3.5px; height: 3.5px; border-radius: 50%; background: var(--bullet);
  }
  .fact-list strong { color: var(--ink); font-weight: 600; }
  .location-map {
    position: absolute; left: 210px; top: 322px; width: 206px; height: 171px;
    background: linear-gradient(135deg, var(--map-light) 0%, var(--map-mid) 100%);
  }

  /* Contact band */
  .contact-band {
    position: absolute; left: 0; bottom: 0; width: 100%;
    background: var(--band); color: var(--white);
  }
  .sheet--plan .contact-band { height: 49px; }
  .sheet--cover .contact-band { height: 46px; }
  .contact-title {
    position: absolute; left: 23px; top: 50%; transform: translateY(-50%);
    font-family: "Encode Sans Condensed", "Arial Narrow", sans-serif;
    font-weight: 400; font-size: 23px; letter-spacing: -0.3px;
    white-space: nowrap;
  }
  .contact-card {
    position: absolute; top: 8px;
    font-size: 6.2px; line-height: 8.2px;
    white-space: nowrap;
  }
  .contact-card .contact-name {
    font-family: "Encode Sans Condensed", "Arial Narrow", sans-serif;
    font-weight: 700; font-size: 6.2px;
  }
  .sheet--plan .contact-card--first { left: 153px; }
  .sheet--plan .contact-card--second { left: 295px; }
  .sheet--cover .contact-card { top: 5px; }
  .sheet--cover .contact-card--first { left: 151px; }
  .sheet--cover .contact-card--second { left: 291px; }

  /* Cover sheet */
  .hero-photo {
    position: absolute; left: 0; top: 0; width: 291px; height: 240px;
    background: linear-gradient(180deg, #5f8fc4 0%, #9fbad6 45%, #a4553f 46%, #8c4a37 70%, #5f7a3a 82%, #4c6530 100%);
  }
  .hero-panel {
    position: absolute; left: 291px; top: 0; width: 141px; height: 240px;
    background: var(--panel); color: var(--white);
  }
  .hero-heading {
    position: absolute; left: 12px; top: 40px;
    font-family: "Encode Sans Condensed", "Arial Narrow", sans-serif;
    font-weight: 400; font-size: 26px; line-height: 29px; letter-spacing: -0.5px;
    white-space: nowrap;
  }
  .metric {
    position: absolute; left: 12px; display: flex; align-items: center; gap: 6px;
  }
  .metric--site { top: 152px; }
  .metric--leasable { top: 196px; }
  .metric svg { width: 15px; height: 15px; margin-top: 6px; }
  .metric-label {
    display: block;
    font-family: "Encode Sans Condensed", "Arial Narrow", sans-serif;
    font-weight: 600; font-size: 6px; color: var(--panel-label); letter-spacing: 0.2px;
  }
  .metric-value {
    display: block;
    font-family: "Encode Sans Condensed", "Arial Narrow", sans-serif;
    font-weight: 600; font-size: 14px; line-height: 15px; color: #e9eaec;
  }
  .gallery-photo { position: absolute; top: 255px; height: 102px; }
  .gallery-photo--one { left: 0; width: 137px; background: linear-gradient(180deg, #4c79b0 0%, #8fb0d2 45%, #3a3d44 50%, #6b5044 70%, #466033 100%); }
  .gallery-photo--two { left: 148px; width: 132px; background: linear-gradient(180deg, #5e88bd 0%, #8c6352 30%, #5a5c62 60%, #9aa6b2 80%, #c8c8c8 100%); }
  .gallery-photo--three { left: 292px; width: 140px; background: linear-gradient(180deg, #1a3768 0%, #2a2d33 40%, #6b5a3c 70%, #2b2c2a 100%); }

  .highlights-title { left: 20px; top: 384px; }
  .highlight-list {
    position: absolute; top: 384px; list-style: none;
    font-size: 7.4px; line-height: 10.1px; color: var(--body-grey);
    white-space: nowrap;
  }
  .highlight-list--left { left: 149px; }
  .highlight-list--right { left: 293px; }
  .highlight-list li { position: relative; padding-left: 9px; }
  .highlight-list li::before {
    content: ""; position: absolute; left: 1px; top: 3.5px;
    width: 3.5px; height: 3.5px; border-radius: 50%; background: var(--bullet);
  }
</style>
</head>
<body>

<section class="sheet sheet--plan">
  <h2 class="section-title plan-title">Site Plan</h2>
  <div class="floor-plan" role="img" aria-label="Main floor plan drawing showing lease space, offices, meeting room, corridors and lobby"></div>

  <h2 class="section-title description-title">Project Description</h2>
  <ul class="fact-list">
    <li><strong>Asking Net Rent</strong> TBD</li>
    <li><strong>Additional Rent</strong> TBD</li>
    <li><strong>Unit Sizes</strong> 2 x (+/-) 1,050 SF and 2 x (+/-) 1,375 SF</li>
    <li><strong>Zoning</strong> - Commercial Mixed-Use</li>
    <li><strong>Available</strong> Spring 2023</li>
    <li><strong>Zoning</strong> - Commercial Mixed-Use</li>
    <li><strong>Available</strong> Spring 2023</li>
    <li><strong>Zoning</strong> - Commercial Mixed-Use</li>
    <li><strong>Available</strong> Spring 2023</li>
    <li><strong>Location</strong> HARBOURLINE BOULEVARD</li>
  </ul>
  <div class="location-map" role="img" aria-label="Street map of the neighbourhood with the site location marked"></div>

  <footer class="contact-band">
    <h2 class="contact-title">Contact Us</h2>
    <div class="contact-card contact-card--first">
      <div class="contact-name">Evan Marlowe</div>
      <div>Vice President &amp; Managing Director</div>
      <div>C +1 555 301 4472 - T +1 555 301 8820</div>
      <div>evan.marlowe@lorvexcrane.com</div>
    </div>
    <div class="contact-card contact-card--second">
      <div class="contact-name">Dana Ostrow</div>
      <div>Vice President</div>
      <div>C +1 555 301 4472 - T +1 555 301 8820</div>
      <div>evan.marlowe@lorvexcrane.com</div>
    </div>
  </footer>
</section>

<section class="sheet sheet--cover">
  <div class="hero-photo" role="img" aria-label="Rendering of a two-storey brick and siding office building with a glass entrance and lawn"></div>
  <div class="hero-panel">
    <h1 class="hero-heading">Commercial<br>Leasing<br>Opportunity</h1>
    <div class="metric metric--site">
      <svg viewBox="0 0 16 16" aria-hidden="true"><rect x="1" y="1" width="14" height="14" rx="1.5" fill="none" stroke="#dcdde0" stroke-width="1.3"/><path d="M4 4 L12 12 M4 4 H7.5 M4 4 V7.5 M12 12 H8.5 M12 12 V8.5" fill="none" stroke="#dcdde0" stroke-width="1.3"/></svg>
      <div><span class="metric-label">SITE SIZE</span><span class="metric-value">2260 SF</span></div>
    </div>
    <div class="metric metric--leasable">
      <svg viewBox="0 0 16 16" aria-hidden="true"><rect x="1" y="1" width="14" height="14" rx="1.5" fill="none" stroke="#dcdde0" stroke-width="1.3"/><path d="M4 4 L12 12 M4 4 H7.5 M4 4 V7.5 M12 12 H8.5 M12 12 V8.5" fill="none" stroke="#dcdde0" stroke-width="1.3"/></svg>
      <div><span class="metric-label">LEASABLE AREA</span><span class="metric-value">960 SF</span></div>
    </div>
  </div>

  <div class="gallery-photo gallery-photo--one" role="img" aria-label="Exterior view of a dark and brick two-storey office building with landscaping"></div>
  <div class="gallery-photo gallery-photo--two" role="img" aria-label="Front entrance of an office building with glass curtain wall and canopy"></div>
  <div class="gallery-photo gallery-photo--three" role="img" aria-label="Office building exterior at dusk with lit entrance"></div>

  <h2 class="section-title highlights-title">Highlights</h2>
  <ul class="highlight-list highlight-list--left">
    <li>Lorem ipsum dolor sit amet</li>
    <li>Consectetur adipiscing elit</li>
    <li>Quisque sit amet est feugiat</li>
    <li>Eeugiat nisl at, sagittis diam</li>
    <li>Sed sed rhoncus nulla</li>
    <li>Id gravida elit.</li>
    <li>In hac habitasse platea dictumst.</li>
    <li>Aliquam in elit est.</li>
    <li>Sed sed rhoncus nulla</li>
    <li>Id gravida elit.</li>
  </ul>
  <ul class="highlight-list highlight-list--right">
    <li>Lorem ipsum dolor sit amet</li>
    <li>Consectetur adipiscing elit</li>
    <li>Quisque sit amet est feugiat</li>
    <li>Eeugiat nisl at, sagittis diam</li>
    <li>Sed sed rhoncus nulla</li>
    <li>Id gravida elit.</li>
    <li>In hac habitasse platea dictumst.</li>
    <li>Aliquam in elit est.</li>
    <li>Sed sed rhoncus nulla</li>
    <li>Id gravida elit.</li>
  </ul>

  <footer class="contact-band">
    <h2 class="contact-title">Contact Us</h2>
    <div class="contact-card contact-card--first">
      <div class="contact-name">Evan Marlowe</div>
      <div>Vice President &amp; Managing Director</div>
      <div>C +1 555 301 4472 - T +1 555 301 8820</div>
      <div>evan.marlowe@lorvexcrane.com</div>
    </div>
    <div class="contact-card contact-card--second">
      <div class="contact-name">Dana Ostrow</div>
      <div>Vice President</div>
      <div>C +1 555 301 4472 - T +1 555 301 8820</div>
      <div>evan.marlowe@lorvexcrane.com</div>
    </div>
  </footer>
</section>

</body>
</html>
```